Word Press Website design

Vantor Webworks is a Website design, SEO, Social Networking and app development company. We would like to see what you can do to create a new, relevant and exciting design for us. This is our first project for Pixel Bazaar so we thought we would test drive this site.  We would like to leave it up to your creative interpretation of the new design, but you can checkout our old design at www.vantorwebcrafters.com
We are always looking for new talent for future projects. Wow us with your designs and there will be future work for you.

Target Market(s)
Our target customers are medium sized businesses of all vertical markets.
Industry/Entity Type
Internet
Requirements
Must have
- Easy to navigate, HTML 5 sliders, modern
Nice to have
- Bring your graphic talents with an outside of the box design that will standout to prospective clients.

```html
<!DOCTYPE html>
<html lang="en">
<head>
<meta charset="utf-8">
<title>Vantor Webworks — Website Design, Kansas City</title>
<link href="https://fonts.googleapis.com/css2?family=Lato:ital,wght@0,400;0,700;0,900;1,700&display=swap" rel="stylesheet">
<style>
:root{
  --ink:#1c1c1c;
  --text:#333;
  --muted:#666;
  --white:#fff;
  --hero-light:#d9dadc;
  --hero-mid:#a9abaf;
  --hero-dark:#7d8086;
  --band-dark:#1e2128;
  --band-mid:#3a3f48;
  --tab-border:#cfcfcf;
  --dot:#444;
}
*{margin:0;padding:0;box-sizing:border-box}
html,body{width:967px;height:1200px;overflow:hidden;background:var(--white)}
body{font-family:'Lato',sans-serif;color:var(--text);position:relative}
.hero{position:absolute;left:0;top:0;width:967px;height:463px;
  background:radial-gradient(ellipse at 70% 35%,var(--hero-light),var(--hero-mid) 60%,var(--hero-dark));
  clip-path:polygon(0 0,100% 0,100% 399px,0 463px)}
.logo{position:absolute;left:69px;top:20px;width:208px;height:87px}
.logo-mark{position:absolute;left:20px;top:0;width:56px;height:56px;background:var(--ink);border-radius:50%}
.logo-name{position:absolute;left:0;bottom:0;width:208px;height:26px;background:var(--ink);color:var(--white);
  font-weight:700;font-size:15px;line-height:26px;text-align:center;border-radius:3px}
.phone{position:absolute;left:670px;top:44px;display:flex;align-items:center;gap:8px;font-size:17px;color:var(--ink)}
.social{position:absolute;left:811px;top:46px;display:flex;gap:8px}
.social span{width:15px;height:15px;border-radius:50%;background:#9a9a9a}
.social span:nth-child(3){background:var(--ink)}
.nav{position:absolute;right:74px;top:86px;display:flex;gap:16px;font-size:12px;color:#444;align-items:center}
.nav .active{font-weight:700;color:var(--ink);border-bottom:2px solid var(--ink);padding-bottom:2px}
.hero-title{position:absolute;left:69px;top:187px;font-weight:700;font-size:26px;line-height:34px;color:#222;letter-spacing:.5px}
.btn{position:absolute;top:327px;width:144px;height:28px;font-size:12px;font-weight:700;text-align:center;line-height:26px}
.btn-outline{left:69px;border:1px solid #333;color:#222}
.btn-solid{left:218px;background:linear-gradient(#333,#000);color:var(--white);border:1px solid #000}
.dots{position:absolute;left:854px;top:430px;display:flex;gap:7px}
.dots span{width:10px;height:10px;border-radius:50%;background:var(--dot)}
.dots span.on{background:var(--white);border:2px solid var(--dot)}
.intro-title{position:absolute;right:70px;top:481px;font-weight:900;font-size:26px;color:var(--ink);letter-spacing:.5px}
.intro-copy{position:absolute;left:150px;right:70px;top:523px;font-size:11px;line-height:13px;text-align:right;color:var(--ink)}
.intro-copy p{margin-bottom:12px}
.tabs{position:absolute;left:71px;top:643px;width:826px;height:32px;display:flex;gap:2px}
.tab{flex:1 1 auto;border:1px solid var(--tab-border);border-radius:2px;background:linear-gradient(#fff,#eee);
  font-size:11px;font-weight:700;color:#333;text-align:center;line-height:30px}
.clients{position:absolute;left:0;top:710px;width:967px;height:404px;
  background:radial-gradient(ellipse at 50% 30%,var(--band-mid),var(--band-dark) 75%)}
.clients-title{position:absolute;top:57px;width:100%;text-align:center;color:var(--white);font-weight:700;font-size:25px}
.clients-rule{position:absolute;left:441px;top:99px;width:85px;height:4px;background:var(--white)}
.quote{position:absolute;left:90px;right:90px;top:143px;text-align:center;color:var(--white);font-style:italic;font-weight:700;font-size:13.5px;line-height:17px}
.client-badge{position:absolute;left:379px;top:237px;width:209px;height:67px;background:var(--white);
  display:flex;align-items:center;justify-content:center;gap:10px;font-weight:700;font-size:19px;color:#1d5f8a}
.client-badge i{width:26px;height:26px;border-radius:50%;background:#1d5f8a}
.client-role{position:absolute;top:323px;width:100%;text-align:center;color:var(--white);font-weight:700;font-size:14px}
.client-org{position:absolute;top:343px;width:100%;text-align:center;color:#eee;font-size:14px}
.footer-links{position:absolute;top:1138px;width:100%;text-align:center;font-size:9.5px;color:#777}
.footer-links .current{color:var(--ink)}
.footer-links b{font-weight:400;margin:0 8px}
.footer-address{position:absolute;top:1161px;width:100%;text-align:center;font-size:9.5px;font-weight:700;color:var(--ink)}
.footer-address b{font-weight:400;margin:0 7px}
</style>
</head>
<body>
<section class="hero" role="img" aria-label="Photo of a businesswoman holding a tablet against a cloudy grey sky with flying letters and banknotes"></section>

<div class="logo">
  <div class="logo-mark"></div>
  <div class="logo-name">VANTOR WEBWORKS, INC.</div>
</div>

<div class="phone">
  <svg width="16" height="16" viewBox="0 0 24 24"><path fill="#1c1c1c" d="M6.6 10.8c1.4 2.8 3.8 5.1 6.6 6.6l2.2-2.2c.3-.3.7-.4 1-.2 1.1.4 2.3.6 3.6.6.6 0 1 .4 1 1V20c0 .6-.4 1-1 1C10.6 21 3 13.4 3 4c0-.6.4-1 1-1h3.5c.6 0 1 .4 1 1 0 1.3.2 2.5.6 3.6.1.3 0 .7-.2 1z"/></svg>
  <span>866.555.0198</span>
</div>
<div class="social"><span></span><span></span><span></span><span></span></div>

<nav class="nav">
  <span class="active">HOME</span><span>ABOUT US</span><span>SERVICES</span><span>PORTFOLIO</span><span>CASE STUDIES</span><span>TESTIMONIALS</span><span>CONTACT US</span>
  <svg width="11" height="11" viewBox="0 0 12 12"><circle cx="5" cy="5" r="4" fill="none" stroke="#222" stroke-width="1.5"/><path d="M8 8l3 3" stroke="#222" stroke-width="1.5"/></svg>
</nav>

<h1 class="hero-title">VANTOR WEBWORKS HAS BEEN<br>DEVELOPING CUSTOM WEBSITES IN<br>KANSAS CITY SINCE 1998.</h1>
<div class="btn btn-outline">LEARN MORE</div>
<div class="btn btn-solid">CONTACT</div>
<div class="dots"><span></span><span class="on"></span><span></span></div>

<h2 class="intro-title">WEBSITE DESIGN, KANSAS CITY</h2>
<div class="intro-copy">
  <p>Vantor Webworks has been developing custom Websites in Kansas City since 1998. We build living, breathing, dynamic Website designs to meet the needs of diverse businesses. Website designers are a dime a dozen. Why pay for what you can get for FREE? Because your time is better spent running your business. Your time and money is valuable, and we can maximize both. Let Vantor Webworks create your next Website because your image matters</p>
  <p>Vantor Webworks creates Websites that will wow your customers and blow away your competition. While browsing the Web, do you ever say “This company looks legitimate?” Your customers make the same snap judgments. We build trustworthy and professional custom Website designs that Kansas City businesses rely upon.</p>
</div>

<div class="tabs">
  <div class="tab">WEBSITE DESIGN</div><div class="tab">HOSTING</div><div class="tab">ECOMMERCE</div><div class="tab">PROGRAMMING</div><div class="tab" style="flex-grow:0;width:100px">SEO</div><div class="tab">PHOTOGRAPHY SERVICES</div>
</div>

<section class="clients" role="img" aria-label="Photo of a group of business people standing behind two hands in a handshake, darkened">
  <h2 class="clients-title">WHAT OUR CLIENTS SAY</h2>
  <div class="clients-rule"></div>
  <p class="quote">“...you guys have gone beyond to make right and to correct what was lost in our first process [with another vendor], while adding a great deal of value on top of it. In addition, you are managing the process with the first vendor in a way that makes you a premier partner with us. Please let [prospective clients] know they can call me anytime.”<br>www.northmarkpartners.com</p>
  <div class="client-badge"><i></i>Northmark Partners</div>
  <div class="client-role">President</div>
  <div class="client-org">Northmark Partners and Talent Growth Institute</div>
</section>

<div class="footer-links"><span class="current">Home</span><b>|</b>Website Design<b>|</b>Hosting<b>|</b>eCommerce<b>|</b>Programming<b>|</b>SEO<b>|</b>Contact Us<b>|</b>About Us<b>|</b>Services<b>|</b>Portfolio<b>|</b>Testimonials<b>|</b>Photography Services</div>
<div class="footer-address">Vantor Webworks, L.L.C.<b>|</b>2840 Orchard Lane<b>|</b>Kansas City, MO 64133<b>|</b>816-555-0142</div>
</body>
</html>
```